Visitenkarten-Design für Immobilien-Unternehmen
Designer ist sehr bemüht und die Änderungswünsche wurden rasch bearbeitet. Auch wurde im Nachhinein noch mein Wunsch auf Adaptierung zu einem Lackdruck bearbeitet und gesendet. Ich bin mit der Abwicklung vollkommen zufrieden - Vielen Dank
Zielgruppe
Die TOLU Immobilien GmbH ist eine durch Ing. Kilian Frühwald inhabergeführte Gesellschaft, welche sich schwerpunktmäßig mit Immobilieninvestitionen sowie Beteiligungen im Bereich von Wohn- und Gewerbeimmobilien beschäftigt. Das Unternehmen kauft, hält, vermietet und verkauft Liegenschaften aller Art, mit dem Fokus auf Gewerbe- und Wohnimmobilien. Zielgruppe sind Personen, welche Immobilien verkaufen möchten - wir betreiben nur eigene Vermögensverwaltung
siehe: www.tolu-immobilien.at
Aufgabenstellung
schlicht und einfach gehalten - weniger ist mehr - nur die wichtigsten Informationen auf der Visitenkarte.
siehe Homepage: www.tolu-immobilien.at

```html
<!DOCTYPE html>
<html lang="de">
<head>
<meta charset="utf-8">
<title>TOLU Immobilien GmbH – Visitenkarte</title>
<link rel="stylesheet" href="https://fonts.googleapis.com/css2?family=Open+Sans:wght@300;400;700&display=swap">
<style>
  :root {
    --canvas: #e6e6e4;
    --card-dark: #2b2a29;
    --card-light: #ffffff;
    --ink: #3a3a3a;
    --ink-strong: #1c1c1c;
    --on-dark: #f4f4f2;
  }
  * { box-sizing: border-box; margin: 0; padding: 0; }
  html, body { width: 1200px; height: 1200px; overflow: hidden; }
  body {
    background: var(--canvas);
    font-family: "Open Sans", Arial, sans-serif;
    display: flex;
    flex-direction: column;
    align-items: center;
    justify-content: center;
    gap: 60px;
  }
  .card {
    width: 860px;
    height: 500px;
    position: relative;
    box-shadow: 0 10px 30px rgba(0,0,0,0.18);
  }

  /* Brand name: one colour, one weight, one plain square */
  .brand {
    display: flex;
    align-items: center;
    gap: 16px;
    font-weight: 400;
    white-space: nowrap;
  }
  .brand__mark {
    width: 18px;
    height: 18px;
    background: currentColor;
    flex: none;
  }

  /* Front */
  .card--front {
    background: var(--card-dark);
    display: flex;
    align-items: center;
    justify-content: center;
  }
  .card--front .brand {
    color: var(--on-dark);
    font-size: 44px;
    letter-spacing: 2px;
  }

  /* Back */
  .card--back {
    background: var(--card-light);
    color: var(--ink);
  }
  .back__left {
    position: absolute;
    left: 64px;
    top: 64px;
    width: 340px;
  }
  .card--back .brand {
    color: var(--ink-strong);
    font-size: 24px;
    letter-spacing: 1px;
    gap: 10px;
  }
  .card--back .brand__mark { width: 11px; height: 11px; }
  .company {
    margin-top: 52px;
    font-size: 21px;
    font-weight: 300;
  }
  .address {
    margin-top: 22px;
    font-size: 21px;
    font-weight: 300;
    line-height: 1.35;
    font-style: normal;
  }
  .divider {
    position: absolute;
    left: 430px;
    top: 100px;
    width: 2px;
    height: 120px;
    background: var(--ink-strong);
  }
  .services {
    position: absolute;
    left: 470px;
    top: 110px;
    list-style: none;
    font-weight: 700;
    font-size: 16px;
    letter-spacing: 1.5px;
    line-height: 1.5;
    color: var(--ink-strong);
  }
  .contact {
    position: absolute;
    left: 470px;
    bottom: 60px;
    font-size: 21px;
    font-weight: 300;
    line-height: 1.4;
    font-style: normal;
  }
  .contact__phone { margin-bottom: 24px; }
</style>
</head>
<body>
  <section class="card card--front" aria-label="Vorderseite">
    <div class="brand">
      <span class="brand__mark"></span>
      <span class="brand__name">TOLU Immobilien GmbH</span>
    </div>
  </section>

  <section class="card card--back" aria-label="Rückseite">
    <div class="back__left">
      <div class="brand">
        <span class="brand__mark"></span>
        <span class="brand__name">TOLU Immobilien GmbH</span>
      </div>
      <p class="company">TOLU Immobilien GmbH</p>
      <address class="address">Birkenfeld 148/2<br>8222 Ostwald</address>
    </div>

    <span class="divider"></span>

    <ul class="services">
      <li>IMMOBILIEN</li>
      <li>INVESTITIONEN</li>
      <li>BETEILIGUNGEN</li>
      <li>LIEGENSCHAFTEN</li>
    </ul>

    <address class="contact">
      <div class="contact__phone">+43 664 480 21 57</div>
      <div>office@tolu-immobilien.at</div>
      <div>www.tolu-immobilien.at</div>
    </address>
  </section>
</body>
</html>
```